Funeral Comparison Website Needs Designer For WireFrame Mock Up (That we've already done)

This should be a pretty quick design project. It's a single page based on a wireframe mockup we did.
Our site (restfulchoices.net) helps people find and compare funeral homes and cemeteries. Our site hasn't been redesigned since we launched in 2008, so it is fairly dated, and we've seen new competitors pop-up in the past year so we need to come up with a fresh redeisgn. We need someone to take our mockup and work their magic with it. As I mentioned this is a single page based on our wireframe mockup.
Please see attached mockup and logo.
Look and feel
Each slider illustrates characteristics of the customer's brand and the style your logo design should communicate.

```html
<!DOCTYPE html>
<html lang="en">
<head>
<meta charset="utf-8">
<title>RestfulChoices – Request Funeral Quotes</title>
<link href="https://fonts.googleapis.com/css2?family=Crimson+Pro:wght@400;600;700&display=swap" rel="stylesheet">
<style>
:root{
  --navy:#191c33;
  --navy-deep:#0e1124;
  --ink:#1c2033;
  --blue:#0077aa;
  --blue-mid:#1a7aa8;
  --green:#3a9a2a;
  --arrow:#66c41e;
  --panel:#f2f2f2;
  --border:#9a9a9a;
  --white:#ffffff;
  --social:#6fa6cf;
}
*{margin:0;padding:0;box-sizing:border-box}
html,body{width:1200px;height:1000px;overflow:hidden;background:var(--white)}
body{position:relative;font-family:"Crimson Pro",Georgia,serif;color:var(--ink)}
.abs{position:absolute}

.site-header{left:16px;top:0;width:1168px;height:60px;background:linear-gradient(#1b1e36 0%,#171a30 70%,#1f5c84 100%)}
.brand{left:364px;top:22px;display:flex;align-items:center;gap:6px}
.brand-dot{width:12px;height:12px;border-radius:50%;background:#3fa0d0}
.brand-name{font-size:17px;font-weight:700;color:#3fa0d0}
.nav{display:flex;font-size:9px;font-weight:700;color:var(--white);text-transform:uppercase;white-space:nowrap}
.nav span{width:69.5px}
.nav-sep{color:#5fa0d0;font-size:10px;line-height:1}
.social{display:flex;gap:4px}
.social i{display:block;width:25px;height:25px;border-radius:4px;background:var(--social)}

.call{width:100px;text-align:center;line-height:1.1}
.call-label{font-size:11.5px;font-weight:600;color:var(--green)}
.call-number{font-size:15px;font-weight:600;color:var(--ink)}

.page-title{left:0;width:1180px;top:84px;text-align:center;font-size:21px;font-weight:400;color:var(--ink);line-height:1.1}
.page-sub{left:0;width:1180px;top:107px;text-align:center;font-size:14px;font-weight:600}
.page-sub .free{color:var(--green)}

.choices{left:369px;top:135px;width:449px;height:149px;display:flex}
.choice{width:150px;height:149px;display:flex;align-items:center;justify-content:center;text-align:center;font-size:14.5px;font-weight:600;line-height:1.05}
.choice-left{padding-right:22px;background:radial-gradient(ellipse at center,#fff 45%,#d9d9d9 80%,#b8b8b8 100%)}
.choice-right{padding-left:30px;background:radial-gradient(ellipse at center,#fff 45%,#d9d9d9 80%,#b8b8b8 100%)}
.choice-dark{background:linear-gradient(#4a4d58 0%,#2a2d3a 12%,#2a2d3a 88%,#4a4d58 100%);color:var(--white)}
.or-box{width:38px;height:39px;background:var(--white);border:2px solid #1f6f9f;display:flex;align-items:center;justify-content:center;font-size:14px;font-weight:600;box-shadow:0 1px 4px rgba(0,0,0,.4)}

.panel{background:var(--panel);border:1px solid var(--border)}
.panel-heading{font-size:19px;font-weight:700;color:var(--ink);line-height:1}

.quote{width:98px;height:71px;background:var(--white);border:1px solid #999;padding:6px 4px 0;font-size:9px;font-weight:700;text-align:center;line-height:1.12}
.quote-by{position:absolute;left:3px;bottom:1px;font-size:6.5px;font-weight:400;text-align:left;line-height:1.2}
.avatar{width:59px;height:50px;border:2px solid #2a7ab0;background:linear-gradient(#c8ccd6,#1c2238)}

.btn{width:114px;height:35px;background:linear-gradient(#2a8ac0 0%,#15507a 55%,#0b1530 100%);color:var(--white);font-size:11.5px;font-weight:600;display:flex;align-items:center;justify-content:center;text-align:center;line-height:1.05;box-shadow:1px 2px 3px rgba(0,0,0,.35)}

.help-card{width:136px;height:160px;background:linear-gradient(var(--blue-mid) 0%,#2d86b4 30%,#e6eef3 72%,#fafafa 100%);padding:13px 12px 0}
.help-title{text-align:center;color:var(--white);font-size:16px;font-weight:400;line-height:1;height:51px;white-space:nowrap}
.help-list{font-size:15px;font-weight:600;color:var(--ink);line-height:1}

.site-footer{left:16px;top:886px;width:1168px;height:114px;background:var(--blue)}
.footer-call .call-label{color:var(--white)}
.footer-call .call-number{color:var(--navy-deep);font-weight:400}
</style>
</head>
<body>

<header class="abs site-header"></header>
<div class="abs brand"><span class="brand-dot"></span><span class="brand-name">RestfulChoices</span></div>
<nav class="abs nav" style="left:495px;top:31px">
  <span>Nav Item</span><span>Nav Item</span><span>Nav Item</span><span>Nav Item</span>
</nav>
<div class="abs nav-sep" style="left:549px;top:29px">'</div>
<div class="abs nav-sep" style="left:620px;top:29px">'</div>
<div class="abs nav-sep" style="left:689px;top:29px">'</div>
<div class="abs social" style="left:773px;top:23px"><i></i><i></i></div>

<div class="abs call" style="left:741px;top:67px">
  <div class="call-label">Give Us A Call.</div>
  <div class="call-number">800.555.0199</div>
</div>

<h1 class="abs page-title">REQUEST FUNERAL QUOTES</h1>
<p class="abs page-sub"><span class="free">Free . No Obligations.</span> Price &amp; Service Quotes.</p>

<section class="abs choices">
  <div class="choice choice-left">I am Planning<br>for the<br>Long Term Future.</div>
  <div class="choice choice-dark">Iam Planning<br>for a&nbsp; Death<br>that will Occur<br>Shortly.</div>
  <div class="choice choice-right">A Death has<br>just Occured.</div>
</section>
<div class="abs or-box" style="left:495px;top:189px">OR</div>
<div class="abs or-box" style="left:649px;top:189px">OR</div>

<svg class="abs" style="left:772px;top:286px" width="58" height="34" viewBox="0 0 58 34">
  <path d="M50 2 C56 12 44 20 22 22 L22 14 L4 25 L22 33 L22 27 C46 26 58 16 50 2 Z" fill="var(--arrow)"/>
</svg>

<section class="abs panel" style="left:353px;top:320px;width:482px;height:169px">
  <h2 class="abs panel-heading" style="left:8px;top:6px">TESTIMONIALS</h2>
  <div class="abs quote" style="left:49px;top:29px">“Text goes here. This is just and example for mock up purposes. Test 1, 2, 3.”<span class="quote-by">Alan Brooks<br>Edmonton, CAN</span></div>
  <div class="abs quote" style="left:192px;top:29px">“Text goes here. This is just and example for mock up purposes. Test 1, 2, 3.”<span class="quote-by">Mara Kellerman<br>Red Deer, CAN</span></div>
  <div class="abs quote" style="left:336px;top:29px">“Text goes here. This is just and example for mock up purposes. Test 1, 2, 3.”<span class="quote-by">Alan Brooks<br>Edmonton, CAN</span></div>
  <div class="abs avatar" style="left:69px;top:104px" role="img" aria-label="Portrait of testimonial author"></div>
  <div class="abs avatar" style="left:212px;top:104px" role="img" aria-label="Portrait of testimonial author"></div>
  <div class="abs avatar" style="left:357px;top:104px" role="img" aria-label="Portrait of testimonial author"></div>
</section>

<svg class="abs" style="left:772px;top:490px" width="58" height="34" viewBox="0 0 58 34">
  <path d="M50 2 C56 12 44 20 22 22 L22 14 L4 25 L22 33 L22 27 C46 26 58 16 50 2 Z" fill="var(--arrow)"/>
</svg>

<section class="abs panel" style="left:353px;top:536px;width:482px;height:336px;background:linear-gradient(var(--panel) 70%,#fcfcfc)">
  <a class="abs btn" style="left:15px;top:8px">Get Started<br>with Pre-planning</a>
  <a class="abs btn" style="left:181px;top:8px">Get Started</a>
  <a class="abs btn" style="left:346px;top:8px">Get Started</a>
  <h2 class="abs panel-heading" style="left:18px;top:72px">SUPPORT CENTER:</h2>
  <div class="abs help-card" style="left:14px;top:121px">
    <h3 class="help-title">QUESTIONS &amp;<br>ANSWERS</h3>
    <p class="help-list">- How we help.<br>- How this works.<br>...</p>
  </div>
  <div class="abs help-card" style="left:171px;top:121px;width:134px">
    <h3 class="help-title">RESOURCES</h3>
    <p class="help-list">- Advice.<br>- Finances.<br>- Planning Guides<br>...</p>
  </div>
  <div class="abs help-card" style="left:325px;top:121px;width:134px;padding:13px 8px 0 10px">
    <h3 class="help-title">GET MORE HELP</h3>
    <p class="help-list">- Learn about our<br>certified consultant.<br>...</p>
  </div>
</section>

<footer class="abs site-footer"></footer>
<nav class="abs nav" style="left:386px;top:899px">
  <span>Nav Item</span><span>Nav Item</span><span>Nav Item</span><span>Nav Item</span>
</nav>
<div class="abs nav-sep" style="left:440px;top:902px;color:var(--navy)">|</div>
<div class="abs nav-sep" style="left:510px;top:902px;color:var(--navy)">|</div>
<div class="abs nav-sep" style="left:579px;top:902px;color:var(--navy)">|</div>
<div class="abs call footer-call" style="left:712px;top:894px">
  <div class="call-label">Give Us A Call.</div>
  <div class="call-number">800.555.0199</div>
</div>
<div class="abs social" style="left:736px;top:930px"><i></i><i></i></div>

</body>
</html>
```